QM Fenwold Detailing, Inc.

I'm looking for business card design for an existing company with an existing logo/website. www.qmfenwold-detailing.com. VETERAN OWNED logo must be present.

Target Market(s)

Structural and architectural steel fabricators

Industry/Entity Type

Structural and architectural steel detailing and engineering

Contact Information for Business Card

logo, business name, address, phone, website, email, employee info

Font styles to use
Serif

Colors
00AB8E
00BBA5
67D7C9
C6EFE9
E9F9F6

Requirements
Must have
• company logo, website, VETERAN OWNED LOGO
Should not have
• Don't make it too busy. Less is more

```html
<!DOCTYPE html>
<html lang="en">
<head>
<meta charset="utf-8">
<title>QM Fenwold Detailing, Inc. – Business Cards</title>
<link rel="stylesheet" href="https://fonts.googleapis.com/css2?family=Open+Sans:wght@400;600;700&display=swap">
<style>
  :root {
    --backdrop: #222222;
    --card: #ffffff;
    --teal-deep: #1a8c9c;
    --teal: #2bb3c2;
    --teal-light: #67c9d3;
    --ink: #111111;
    --grey: #5e5e5e;
    --badge: #c9d3e6;
  }
  * { margin: 0; padding: 0; box-sizing: border-box; }
  html, body { width: 1200px; height: 711px; overflow: hidden; }
  body {
    background: var(--backdrop);
    font-family: "Open Sans", sans-serif;
    position: relative;
  }
  .card {
    position: absolute;
    width: 540px;
    height: 309px;
    background: var(--card);
    box-shadow: 0 12px 26px rgba(0,0,0,.55);
  }
  .card--front { left: 36px; top: 201px; }
  .card--back  { left: 624px; top: 201px; }

  /* Front */
  .front-brand {
    position: absolute; inset: 0;
    display: flex; flex-direction: column; align-items: center; justify-content: center;
    gap: 14px;
  }
  .brand-mark {
    width: 64px; height: 64px; border-radius: 50%;
    background: var(--teal);
  }
  .brand-name {
    font-weight: 700; color: var(--teal-deep);
    font-size: 34px; letter-spacing: 1px; text-align: center; line-height: 1.1;
  }

  /* Back */
  .back-brand {
    position: absolute; left: 24px; top: 70px; width: 220px;
    display: flex; flex-direction: column; align-items: center; gap: 10px;
  }
  .back-brand .brand-mark { width: 44px; height: 44px; }
  .back-brand .brand-name { font-size: 20px; }
  .divider {
    position: absolute; left: 262px; top: 50px; width: 1px; height: 160px;
    background: var(--teal-light);
  }
  .employee {
    position: absolute; left: 286px; top: 50px; width: 240px;
  }
  .employee-name {
    font-size: 25px; font-weight: 700; color: var(--teal); line-height: 1.1;
  }
  .employee-title {
    font-size: 12.5px; font-weight: 600; color: var(--ink); margin-top: 2px;
  }
  .contact-list { list-style: none; margin-top: 18px; }
  .contact-list li {
    display: flex; align-items: center; gap: 8px;
    font-size: 11.5px; color: var(--ink); line-height: 1.6;
  }
  .contact-list svg { width: 11px; height: 11px; flex: none; }
  .address {
    position: absolute; left: 120px; bottom: 30px;
    font-size: 12.5px; color: var(--ink);
  }
  .veteran-badge {
    position: absolute; right: 26px; bottom: 62px;
    width: 52px; height: 46px; background: var(--badge);
  }
</style>
</head>
<body>
  <section class="card card--front">
    <div class="front-brand">
      <span class="brand-mark"></span>
      <span class="brand-name">QM FENWOLD<br>DETAILING</span>
    </div>
  </section>

  <section class="card card--back">
    <div class="back-brand">
      <span class="brand-mark"></span>
      <span class="brand-name">QM FENWOLD<br>DETAILING</span>
    </div>
    <div class="divider"></div>
    <div class="employee">
      <p class="employee-name">Employee Name</p>
      <p class="employee-title">Managing Director</p>
      <ul class="contact-list">
        <li>
          <svg viewBox="0 0 12 12"><path d="M3 1l2 2-1 1.5a6 6 0 0 0 3.5 3.5L9 7l2 2-1.5 2C5 11 1 7 1 2.5z" fill="#2bb3c2"/></svg>
          555.014.2287
        </li>
        <li>
          <svg viewBox="0 0 12 12"><circle cx="6" cy="6" r="5" fill="none" stroke="#2bb3c2" stroke-width="1.3"/><path d="M1 6h10M6 1c-2.5 3-2.5 7 0 10M6 1c2.5 3 2.5 7 0 10" fill="none" stroke="#2bb3c2" stroke-width="1"/></svg>
          www.qmfenwold-detailing.com
        </li>
        <li>
          <svg viewBox="0 0 12 12"><rect x="1" y="2.5" width="10" height="7" fill="none" stroke="#2bb3c2" stroke-width="1.3"/><path d="M1 2.5l5 4 5-4" fill="none" stroke="#2bb3c2" stroke-width="1.2"/></svg>
          sales@qmfenwold-detailing.com
        </li>
      </ul>
    </div>
    <div class="veteran-badge" role="img" aria-label="Veteran owned business badge"></div>
    <p class="address">4810 Harbor Crest Blvd., ste 310 Tampa, FL 33609</p>
  </section>
</body>
</html>
```